Emergency and Referral Vet Hospital promotional sticker design

We're looking at getting some stickers designed that we could give to clients to put on their cars for promotion and advertising. If they could also be suitable for a goodie bag for conference too that would be great. I like the look of water-colour backgrounds, we'll need to include our logo and probably our address (Unit 4/372 Tarvenny Drive Success). We also have a hospital motto "... because they're family" if that could somehow be integrated, we only care for small animals (dogs, cats etc) but the design is very open to suggestion. Would love to see what you can create.

Industry/Entity Type

Veterinary

Colors
0054AA
0677BA
7BADD7
CADEEF
E8F1F8
0094D4
00A9DD
6FCCEA
C7EBF8
E9F6FB

Requirements
Nice to have
• Think beach vibes, blues maybe paw print shapes etc

```html
<!DOCTYPE html>
<html lang="en">
<head>
<meta charset="utf-8">
<title>Shorewell Vet Hospital – Sticker Set</title>
<link href="https://fonts.googleapis.com/css2?family=Lilita+One&family=Poppins:wght@600;700&display=swap" rel="stylesheet">
<style>
  :root {
    --stage: #eef2f5;
    --frame-purple: #6434a0;
    --paper: #ffffff;
    --navy: #0e4a6e;
    --teal: #12bdb4;
    --ink: #111820;
    --photo-warm: #d9913f;
    --photo-cool: #6b7280;
    --photo-light: #f2e3cf;
  }
  * { margin: 0; padding: 0; box-sizing: border-box; }
  html, body { width: 1200px; height: 1200px; overflow: hidden; }
  body { background: var(--stage); position: relative; font-family: "Poppins", sans-serif; }

  .sticker { position: absolute; background: var(--frame-purple); }
  .sticker--square { left: 70px; top: 100px; width: 560px; height: 560px; border-radius: 72px; }
  .sticker--round { left: 540px; top: 500px; width: 600px; height: 600px; border-radius: 50%; }

  .sticker__face {
    position: absolute; inset: 28px; background: var(--paper); overflow: hidden;
  }
  .sticker--square .sticker__face { border-radius: 48px; }
  .sticker--round .sticker__face { border-radius: 50%; }

  .sticker__shapes { position: absolute; inset: 0; width: 100%; height: 100%; }

  .brand-name {
    position: absolute; font-family: "Poppins", sans-serif; font-weight: 700;
    color: var(--ink); font-size: 32px; letter-spacing: 0.5px; line-height: 1;
  }
  .brand-name__dot {
    display: inline-block; width: 14px; height: 14px; border-radius: 50%;
    background: var(--teal); margin-right: 8px; vertical-align: middle;
  }

  .motto {
    position: absolute; font-family: "Lilita One", sans-serif; color: var(--navy);
    line-height: 1; white-space: nowrap;
    text-shadow: 3px 3px 0 #fff, 5px 5px 0 var(--navy);
  }
  .motto__line { display: block; }

  .photo-area {
    position: absolute;
    background: linear-gradient(90deg, var(--photo-warm) 0%, var(--photo-light) 45%, var(--photo-warm) 65%, var(--photo-cool) 100%);
  }

  .address {
    position: absolute; color: #fff; font-weight: 700; font-size: 20px;
    white-space: nowrap; transform-origin: left top;
  }

  /* square layout */
  .sticker--square .brand-name { left: 40px; top: 110px; }
  .sticker--square .motto { left: 60px; top: 180px; font-size: 62px; }
  .sticker--square .motto__line + .motto__line { margin-left: -30px; margin-top: 6px; }
  .sticker--square .photo-area { left: 0; top: 360px; width: 430px; height: 144px; border-top-right-radius: 40px; }
  .sticker--square .address { left: 470px; top: 470px; transform: rotate(-90deg); }

  /* round layout */
  .sticker--round .brand-name { left: 240px; top: 170px; }
  .sticker--round .motto { left: 66px; top: 230px; font-size: 66px; }
  .sticker--round .motto__line:first-child { margin-left: 60px; }
  .sticker--round .motto__line + .motto__line { margin-top: 6px; }
  .sticker--round .photo-area { left: 90px; top: 390px; width: 420px; height: 180px; border-top-right-radius: 60px; }
  .curved-address { font-family: "Poppins", sans-serif; font-weight: 700; font-size: 19px; fill: var(--navy); }
</style>
</head>
<body>

  <div class="sticker sticker--square">
    <div class="sticker__face">
      <svg class="sticker__shapes" viewBox="0 0 504 504" aria-hidden="true">
        <path d="M380 0 H504 V504 H420 C470 380 470 240 440 140 C420 80 400 40 380 0 Z" fill="var(--navy)"/>
        <path d="M0 360 C60 330 140 340 200 380 C250 410 300 420 360 400 V504 H0 Z" fill="var(--teal)"/>
      </svg>
      <div class="brand-name"><span class="brand-name__dot"></span>Shorewell</div>
      <div class="motto">
        <span class="motto__line">... because</span>
        <span class="motto__line">they're family</span>
      </div>
      <div class="photo-area" role="img" aria-label="Photo of a beagle, a hamster, a ginger kitten and a grey French bulldog"></div>
      <div class="address">Unit 4/372 Tarvenny Drive Success</div>
    </div>
  </div>

  <div class="sticker sticker--round">
    <div class="sticker__face">
      <svg class="sticker__shapes" viewBox="0 0 544 544" aria-hidden="true">
        <defs>
          <path id="address-arc" d="M40 272 A232 232 0 0 1 272 40"/>
        </defs>
        <path d="M360 0 H544 V544 H500 C520 420 500 280 440 160 C410 100 385 50 360 0 Z" fill="var(--navy)"/>
        <path d="M0 400 C70 380 140 390 200 420 C260 450 320 460 400 440 V544 H0 Z" fill="var(--teal)"/>
        <text class="curved-address"><textPath href="#address-arc" startOffset="2%">Unit 4/372 Tarvenny Drive Success</textPath></text>
      </svg>
      <div class="brand-name"><span class="brand-name__dot"></span>Shorewell</div>
      <div class="motto">
        <span class="motto__line">... because</span>
        <span class="motto__line">they're family</span>
      </div>
      <div class="photo-area" role="img" aria-label="Photo of a beagle, a hamster, a ginger kitten and a grey French bulldog"></div>
    </div>
  </div>

</body>
</html>
```